BrightLedger, The Ultimate Franchise Online Training Platform

Need Roll-up Banner Design measuring 30 x 80 inches, Looking for a design that is clean, professional, not cliche. We’re open to shape motifs like a circle, square, or swoosh—choose what best reinforces motion, strength, or innovation. Consistency is key: this should look great whether it's on a banner, a slide deck, or our letterhead. Our business is serving as a Franchisee e-learning platform providing vetted information from experts, an online library and masterclasses. Uploaded examples of Banner art with correct wording. Wording can be:
THE ULTIMATE FRANCHISEE TOOLKIT
Your 24/7 Edge for Franchise Success
On-Demand Resource Library
Monthly Masterclasses
Direct Access to Industry Experts
“Your Entrepreneurial Edge.”
OR
“Opening your first or your fifth, BrightLedger is your unfair advantage.”
Catapult your learning curve.
Avoid costly mistakes.
Grow with a community that gets it.
Join the Movement. Unlock Your Toolkit Today.
Updates

My apologies to designers I haven´t voted or provided updates for yet. We are still reviewing designs as the last call will be made by the owners and we live in different time zones. Thank you!

Target Market(s)

Business Owners, from small to mid

Industry/Entity Type

Small Business Owners, Franchisees

Font styles to use
Other font styles liked:
• Poppins, Roboto, Garamond, Montserrat, Lato

Colors

Designer to choose colors to be used in the design.

Requirements
Must have
• Consistency in color guide, font and wording
Nice to have
• Open to pretty much fluid designs, simple and uncluttered

```html
<!DOCTYPE html>
<html lang="en">
<head>
<meta charset="utf-8">
<title>BrightLedger Roll-up Banners</title>
<link href="https://fonts.googleapis.com/css2?family=Montserrat:wght@300;400;600;800;900&family=Poppins:wght@300;400;700;800&display=swap" rel="stylesheet">
<style>
  :root {
    --backdrop: #d9dad8;
    --paper: #ffffff;
    --mist: #f1f2f0;
    --ink: #1f2419;
    --forest: #272d20;
    --lime: #a8cd3c;
    --lime-soft: #b7cf7a;
    --slate: #5a5c57;
    --slate-mid: #72756e;
    --slate-dark: #5d605a;
    --cta-text: #3b4232;
  }
  * { margin: 0; padding: 0; box-sizing: border-box; }
  html, body { width: 1200px; height: 1200px; overflow: hidden; }
  body {
    background: var(--backdrop);
    position: relative;
    font-family: "Poppins", sans-serif;
  }
  .banner { position: absolute; overflow: hidden; }
  .banner > * { position: absolute; }
  .center-line { left: 0; width: 100%; text-align: center; white-space: nowrap; }

  /* ---------- Main banner ---------- */
  .banner--main {
    left: 422px; top: 113px; width: 383px; height: 1020px;
    background: var(--paper);
  }
  .banner--main .shapes { left: 0; top: 0; width: 383px; height: 1020px; }
  .headline-top {
    top: 54px; font-family: "Montserrat", sans-serif; font-weight: 900;
    font-size: 38px; letter-spacing: 2px; color: var(--ink);
  }
  .headline-mid {
    top: 100px; font-family: "Montserrat", sans-serif; font-weight: 300;
    font-size: 53px; color: var(--lime); letter-spacing: 0.5px;
  }
  .headline-main {
    top: 143px; font-family: "Montserrat", sans-serif; font-weight: 900;
    font-size: 70px; color: var(--ink); letter-spacing: 1px;
  }
  .brand-block {
    left: 56px; top: 274px; width: 256px; height: 256px;
    background: var(--lime);
    display: flex; flex-direction: column; justify-content: center; align-items: center;
    font-family: "Montserrat", sans-serif; font-weight: 400; font-size: 52px;
    line-height: 1.1; color: var(--ink);
  }
  .benefits { top: 580px; }
  .benefits p { font-size: 17px; line-height: 1; margin-bottom: 14px; }
  .benefits .strong { color: var(--paper); font-weight: 800; }
  .benefits .light { color: var(--lime); font-family: "Montserrat", sans-serif; font-weight: 400; font-size: 17.5px; }
  .benefits .hero { margin-bottom: 6px; }
  .benefits .hero b { font-size: 34px; font-weight: 800; vertical-align: -3px; }
  .footer-brand {
    left: 174px; top: 872px; display: flex; align-items: center; gap: 8px;
    font-family: "Montserrat", sans-serif; font-weight: 400; font-size: 26px; color: var(--ink);
  }
  .footer-brand .mark { width: 22px; height: 22px; background: var(--lime); }
  .site {
    font-family: "Poppins", sans-serif; font-weight: 800; color: var(--ink);
  }
  .site .accent { color: var(--lime); }
  .banner--main .site { top: 944px; font-size: 27px; }

  /* ---------- Side banners ---------- */
  .banner--side {
    top: 321px; width: 270px; height: 721px;
    background: linear-gradient(to bottom, var(--mist) 0, var(--mist) 277px, var(--slate-mid) 277px, var(--slate-dark) 555px);
  }
  .banner--left { left: 66px; }
  .banner--right { left: 872px; }
  .opening {
    top: 44px; font-family: "Montserrat", sans-serif; font-weight: 800;
    font-size: 40px; color: var(--slate);
  }
  .first-line, .fifth-line {
    font-family: "Montserrat", sans-serif; font-size: 25px; font-weight: 400; color: var(--slate);
  }
  .first-line { top: 91px; color: var(--lime-soft); }
  .fifth-line { top: 123px; }
  .first-line b, .fifth-line b { font-weight: 800; }
  .fifth-line small { font-size: 17px; }
  .side-block {
    left: 44px; top: 183px; width: 181px; height: 181px; background: var(--lime-soft);
    display: flex; flex-direction: column; justify-content: center; align-items: center;
    font-family: "Montserrat", sans-serif; font-weight: 400; font-size: 38px;
    line-height: 1.1; color: var(--slate);
  }
  .advantage {
    top: 392px; font-family: "Montserrat", sans-serif; font-weight: 300;
    font-size: 28px; line-height: 32px; color: #f2f2f0;
  }
  .points { top: 470px; left: 0; width: 100%; }
  .points p {
    font-family: "Montserrat", sans-serif; font-weight: 400; font-size: 10.5px;
    color: var(--lime-soft); text-align: center; height: 27px; line-height: 17px;
  }
  .points p + p { border-top: 1px solid var(--lime-soft); margin: 0 32px; padding-top: 9px; }
  .points p:last-child { margin: 0; border: 0; padding-top: 9px; position: relative; }
  .points p:last-child::before {
    content: ""; position: absolute; left: 32px; right: 32px; top: 0; border-top: 1px solid var(--lime-soft);
  }
  .cta-band {
    left: 0; top: 555px; width: 270px; height: 90px; background: var(--lime-soft);
    display: flex; flex-direction: column; justify-content: center; align-items: center;
    font-family: "Montserrat", sans-serif; font-weight: 800; font-size: 19.5px;
    line-height: 25px; color: var(--cta-text);
  }
  .cta-tail { left: 160px; top: 644px; width: 76px; height: 24px; }
  .banner--side .site { top: 674px; font-size: 18.5px; color: #ecedea; }
  .banner--side .site .accent { color: var(--lime-soft); }
</style>
</head>
<body>

  <section class="banner banner--side banner--left">
    <p class="opening center-line">OPENING</p>
    <p class="first-line center-line">YOUR <b>FIRST</b></p>
    <p class="fifth-line center-line"><small>OR</small> YOUR <b>FIFTH,</b></p>
    <div class="side-block"><span>Bright</span><span>Ledger</span></div>
    <p class="advantage center-line">IS YOUR UNFAIR<br>ADVANTAGE.</p>
    <div class="points">
      <p>CATAPULT YOUR LEARNING CURVE.</p>
      <p>AVOID COSTLY MISTAKES.</p>
      <p>GROW WITH A COMMUNITY THAT GETS IT.</p>
    </div>
    <div class="cta-band"><span>JOIN THE MOVEMENT</span><span>UNLOCK YOUR</span><span>TOOLKIT TODAY</span></div>
    <svg class="cta-tail" viewBox="0 0 76 24" aria-hidden="true"><polygon points="14,0 76,0 0,24" fill="#b7cf7a"/></svg>
    <p class="site center-line">www.BRIGHT<span class="accent">LEDGER</span>.com</p>
  </section>

  <section class="banner banner--main">
    <svg class="shapes" viewBox="0 0 478 1274" preserveAspectRatio="none" aria-hidden="true">
      <polygon points="0,683 478,459 478,937 352,999 0,1159" fill="#272d20"/>
      <polygon points="0,979 124,1103 0,1159" fill="#a8cd3c"/>
      <polygon points="352,999 478,937 478,1069" fill="#a8cd3c"/>
    </svg>
    <p class="headline-top center-line">THE ULTIMATE</p>
    <p class="headline-mid center-line">FRANCHISEE</p>
    <p class="headline-main center-line">TOOLKIT</p>
    <div class="brand-block"><span>Bright</span><span>Ledger</span></div>
    <div class="benefits center-line">
      <p class="strong hero">Your <b>24/7</b> Edge for</p>
      <p class="strong">Franchise Success</p>
      <p class="light">On-Demand Resource Library</p>
      <p class="strong">Monthly Masterclasses</p>
      <p class="light">Direct Access to Industry Experts</p>
      <p class="strong">Your Entrepreneurial Edge.</p>
    </div>
    <div class="footer-brand"><span class="mark"></span><span>BrightLedger</span></div>
    <p class="site center-line">www.BRIGHT<span class="accent">LEDGER</span>.com</p>
  </section>

  <section class="banner banner--side banner--right">
    <p class="opening center-line">OPENING</p>
    <p class="first-line center-line">YOUR <b>FIRST</b></p>
    <p class="fifth-line center-line"><small>OR</small> YOUR <b>FIFTH,</b></p>
    <div class="side-block"><span>Bright</span><span>Ledger</span></div>
    <p class="advantage center-line">IS YOUR UNFAIR<br>ADVANTAGE.</p>
    <div class="points">
      <p>CATAPULT YOUR LEARNING CURVE.</p>
      <p>AVOID COSTLY MISTAKES.</p>
      <p>GROW WITH A COMMUNITY THAT GETS IT.</p>
    </div>
    <div class="cta-band"><span>JOIN THE MOVEMENT</span><span>UNLOCK YOUR</span><span>TOOLKIT TODAY</span></div>
    <svg class="cta-tail" viewBox="0 0 76 24" aria-hidden="true"><polygon points="14,0 76,0 0,24" fill="#b7cf7a"/></svg>
    <p class="site center-line">www.BRIGHT<span class="accent">LEDGER</span>.com</p>
  </section>

</body>
</html>
```